Business Cards for Tech Company - Corvane

We would like new modern business cards designed for our company. Attached are some examples of other business cards we like. <br/><br/>Info we need is: <br/>First Name, Last Name<br/>Address<br/>Store Phone<br/>Cell Phone<br/>Email Address<br/>Text Logo <br/>And Other Logo<br/>

Industry/Entity Type

Technology Equipment

Contact Information for Business Card

Please use these details as example:

Dale Morrow
Technology Specialist
Direct 555.617.2094
Phone 555-730-8186

dale.morrow@corvane.example

2971 Willet Lane
Fenmoor, OR 00427

Font styles to use
Sans Serif
Other font styles liked:
• Anything easy to read and modern

Colors

Designer to choose colors to be used in the design.

Requirements
Must have
• Both Logos
• Signature as name
• Use the text logo and use the shark logo but do not use the full shark logo. Have it where it is zoomed in and is expanding out of the card.
Nice to have
• Keep it clean and modern
• We like blue, white, and black/grays.
Should not have
• Random icons for phone and address.

```html
<!DOCTYPE html>
<html lang="en">
<head>
<meta charset="UTF-8">
<title>Corvane Business Cards</title>
<link rel="stylesheet" href="https://fonts.googleapis.com/css2?family=Saira:wght@300;400;500;700&display=swap">
<style>
  :root {
    --bg: #b1b1b1;
    --card-white: #f4f4f4;
    --card-black: #171717;
    --brand-blue: #1f74e6;
    --logo-grey: #5a5a5a;
    --text-light: #f2f2f2;
    --text-muted: #9a9a9a;
    --text-soft: #cfcfcf;
    --rule: #3a3a3a;
  }
  * { box-sizing: border-box; margin: 0; padding: 0; }
  html, body {
    width: 1077px;
    height: 1200px;
    overflow: hidden;
    background: var(--bg);
    font-family: "Saira", "Helvetica Neue", Arial, sans-serif;
  }
  .canvas {
    position: relative;
    width: 1077px;
    height: 1200px;
  }
  .card {
    position: absolute;
    left: 198px;
    width: 680px;
    height: 388px;
    overflow: hidden;
    box-shadow: 0 18px 40px rgba(0,0,0,0.22);
  }
  /* Front */
  .card-front {
    top: 150px;
    background: var(--card-white);
  }
  .corner {
    position: absolute;
    width: 150px;
    height: 150px;
  }
  .corner-top-right { top: 0; right: 0; }
  .corner-bottom-left { bottom: 0; left: 0; }
  .wordmark {
    position: absolute;
    inset: 0;
    display: flex;
    align-items: center;
    justify-content: center;
    font-weight: 700;
    font-size: 64px;
    letter-spacing: -1px;
    color: var(--logo-grey);
  }
  /* Back */
  .card-back {
    top: 662px;
    background: var(--card-black);
    color: var(--text-light);
  }
  .identity {
    position: absolute;
    left: 40px;
    top: 44px;
    width: 270px;
  }
  .person-name {
    font-size: 34px;
    font-weight: 400;
    line-height: 1;
  }
  .person-title {
    margin-top: 6px;
    font-size: 15px;
    font-weight: 400;
    color: var(--brand-blue);
  }
  .phones {
    margin-top: 34px;
    font-size: 17px;
    line-height: 1.5;
  }
  .phones .label {
    display: inline-block;
    width: 62px;
    color: var(--text-muted);
  }
  .divider {
    position: absolute;
    left: 330px;
    top: 60px;
    width: 1px;
    height: 250px;
    background: var(--rule);
  }
  .details {
    position: absolute;
    left: 360px;
    top: 78px;
    font-size: 15px;
    line-height: 1.45;
  }
  .details .web { font-weight: 500; }
  .details .email { color: var(--text-soft); }
  .address {
    margin-top: 26px;
    color: var(--text-soft);
  }
  .signature {
    position: absolute;
    left: 400px;
    top: 262px;
    width: 200px;
    height: 46px;
    border-radius: 6px;
    background: linear-gradient(90deg, rgba(216,216,216,0.18), rgba(216,216,216,0.32));
  }
  .brand-dot {
    position: absolute;
    right: 36px;
    bottom: 32px;
    width: 26px;
    height: 26px;
    border-radius: 50%;
    background: var(--brand-blue);
  }
</style>
</head>
<body>
<main class="canvas">
  <section class="card card-front" aria-label="Card front">
    <svg class="corner corner-top-right" viewBox="0 0 150 150" aria-hidden="true">
      <polygon points="60,0 150,0 150,150" fill="var(--brand-blue)"/>
    </svg>
    <svg class="corner corner-bottom-left" viewBox="0 0 150 150" aria-hidden="true">
      <polygon points="0,0 90,150 0,150" fill="var(--brand-blue)"/>
    </svg>
    <div class="wordmark">Corvane</div>
  </section>

  <section class="card card-back" aria-label="Card back">
    <div class="identity">
      <h1 class="person-name">Dale Morrow</h1>
      <p class="person-title">Technology Specialist</p>
      <p class="phones">
        <span class="label">Direct:</span>555.617.2094<br>
        <span class="label">Phone:</span>555-730-8186
      </p>
    </div>
    <div class="divider"></div>
    <div class="details">
      <p class="web">www.corvane.example</p>
      <p class="email">dale.morrow@corvane.example</p>
      <p class="address">2971 Willet Lane<br>Fenmoor, OR 00427</p>
    </div>
    <div class="signature" role="img" aria-label="Handwritten signature of Dale Morrow"></div>
    <div class="brand-dot" aria-hidden="true"></div>
  </section>
</main>
</body>
</html>
```